Roofing Company Modern look

I want a modern and sophisticated look for our roofing business.

Our address is :

5172 Maple Crane Rd
Cedar Hollow, Fl 34790

(407)-555-2719

www.SummitPeakRoofs.example

I also want to make sure on the back there is a spot to put
Project Manager Name :

Number:

Because the cards will be used by all sales people

Project Manager Name :

Also there are accreditation we have logos are uploaded here as well that I would like maybe on the back of card as well

I also want to highlight our special attributions or trades:

Residential & Commercial
Fully Insured
License # CCC8274916
Insurance Claims
Serving Central Florida Since 1992
Free Estimates

Contact Information for Business Card

Our address is :

5172 Maple Crane Rd
Cedar Hollow, Fl 34790

(407)-555-2719

Project Manager Name :

Residential & Commercial
Fully Insured
License # CCC8274916
Insurance Claims
Free Estimates

Font styles to use
Serif
Sans Serif

Colors
3176b5

Requirements
Must have
• Must have royal blue like my logo grey and black are the colors I like

```html
<!DOCTYPE html>
<html lang="en">
<head>
<meta charset="utf-8">
<title>Summit Peak Roofing &amp; Gutters – Business Card</title>
<link rel="stylesheet" href="https://fonts.googleapis.com/css2?family=Arimo:wght@400;700&display=swap">
<style>
  :root {
    --royal-blue: #3176b5;
    --bright-blue: #1e88d8;
    --card-black: #232323;
    --card-dark: #2b2b2b;
    --grey: #bdbdbd;
    --light-grey: #d8d8d8;
    --white: #ffffff;
    --page-bg: #1a1a1a;
  }
  * { box-sizing: border-box; margin: 0; padding: 0; }
  html, body {
    width: 1200px; height: 1015px; overflow: hidden;
    background: var(--page-bg);
    font-family: "Arimo", Arial, sans-serif;
  }
  .canvas { position: relative; width: 1200px; height: 1015px; }

  .card {
    position: absolute; left: 250px; width: 700px; height: 400px;
    overflow: hidden; border-radius: 2px;
    box-shadow: 0 18px 40px rgba(0,0,0,.6);
  }

  /* ---------- Front ---------- */
  .card-front { top: 70px; background: var(--white); }
  .front-header {
    position: absolute; inset: 0 0 auto 0; height: 170px;
    background: var(--card-black);
    border-bottom: 6px solid var(--bright-blue);
    display: flex; align-items: center; padding-left: 70px; gap: 22px;
  }
  .brand-dot {
    width: 78px; height: 78px; border-radius: 50%;
    background: var(--bright-blue);
  }
  .brand-name { color: var(--bright-blue); font-weight: 700; line-height: 1.05; }
  .brand-name .main { display: block; font-size: 52px; letter-spacing: 3px; }
  .brand-name .sub { display: block; font-size: 19px; letter-spacing: 2px; }

  .name-field {
    position: absolute; left: 90px; right: 110px; top: 218px;
    display: flex; align-items: flex-end; gap: 14px;
  }
  .name-field .label { color: var(--light-grey); font-weight: 700; font-size: 20px; letter-spacing: 1px; }
  .name-field .line { flex: 1; border-bottom: 1px solid var(--light-grey); height: 1px; margin-bottom: 5px; }

  .badges {
    position: absolute; left: 0; right: 0; top: 285px;
    display: flex; justify-content: center; align-items: center; gap: 50px;
  }
  .badge-hex { width: 120px; height: 80px; clip-path: polygon(20% 0,80% 0,100% 50%,80% 100%,20% 100%,0 50%); background: #1f4f8c; }
  .badge-rect { width: 160px; height: 44px; background: #c9262c; border: 3px solid #1c2d6b; }
  .badge-tall { width: 70px; height: 90px; border-radius: 8px; background: var(--white); border: 3px solid var(--royal-blue); }

  /* ---------- Back ---------- */
  .card-back { top: 545px; background: var(--card-dark); }
  .back-art {
    position: absolute; left: 0; top: 0; width: 330px; height: 400px;
    background: radial-gradient(ellipse at 55% 40%, rgba(30,136,216,.55), rgba(30,136,216,.12) 45%, transparent 70%),
                radial-gradient(ellipse at 45% 80%, rgba(200,200,200,.28), transparent 55%);
  }
  .contact { position: absolute; left: 350px; top: 48px; color: var(--white); font-size: 19px; line-height: 1.3; }
  .contact .address { margin-bottom: 16px; }
  .contact .row { display: flex; align-items: center; gap: 8px; }
  .contact .row svg { width: 16px; height: 16px; flex: none; }
  .divider { width: 180px; border-bottom: 1px solid #777; margin: 14px 0 14px 40px; }
  .attributes { list-style: none; }
  .attributes li { display: flex; align-items: center; gap: 10px; }
  .attributes li::before {
    content: ""; width: 9px; height: 9px; border-radius: 50%;
    background: var(--bright-blue); flex: none;
  }
</style>
</head>
<body>
<main class="canvas">

  <section class="card card-front" aria-label="Card front">
    <header class="front-header">
      <span class="brand-dot"></span>
      <div class="brand-name">
        <span class="main">SUMMIT PEAK</span>
        <span class="sub">ROOFING &amp; GUTTERS LLC</span>
      </div>
    </header>

    <div class="name-field">
      <span class="label">NAME:</span>
      <span class="line"></span>
    </div>

    <div class="badges">
      <div class="badge-hex" role="img" aria-label="Shingle applicator certification badge"></div>
      <div class="badge-rect" role="img" aria-label="Authorized roofing contractor badge"></div>
      <div class="badge-tall" role="img" aria-label="Accredited business rating badge"></div>
    </div>
  </section>

  <section class="card card-back" aria-label="Card back">
    <div class="back-art" role="img" aria-label="Large decorative brand artwork in blue and grey"></div>

    <div class="contact">
      <p class="address">5172 Maple Crane Rd<br>Cedar Hollow, Fl 34790</p>
      <p class="row">
        <svg viewBox="0 0 16 16" aria-hidden="true"><path d="M3 1.5l3 3-1.6 1.8a9 9 0 0 0 5.3 5.3L11.5 10l3 3-1.8 1.8C7 14.5 1.5 9 1.2 3.3z" fill="#1e88d8"/></svg>
        (407)-555-2719
      </p>
      <p class="row">
        <svg viewBox="0 0 16 16" aria-hidden="true"><circle cx="8" cy="8" r="6.5" fill="none" stroke="#1e88d8" stroke-width="1.5"/><path d="M1.5 8h13M8 1.5c-3 3.5-3 9.5 0 13M8 1.5c3 3.5 3 9.5 0 13" fill="none" stroke="#1e88d8" stroke-width="1.2"/></svg>
        www.SummitPeakRoofs.example
      </p>
      <div class="divider"></div>
      <ul class="attributes">
        <li>Residential &amp; Commercial</li>
        <li>Fully Insured</li>
        <li>License # CCC8274916</li>
        <li>Insurance Claims</li>
        <li>Serving Central Florida Since 1992</li>
        <li>Free Estimates</li>
      </ul>
    </div>
  </section>

</main>
</body>
</html>
```